Business Card Design Project

We need a business card design template for a direct sales company that is branded to the company but the name information can be changed for the representatives. The card needs to include the company logo and website...www.myvelsane.example. It should also include the Customer Service number which is 1-800-472-Velsan.

The front should have a space with the name and a place for their phone contact information and email address.
Updates

The card should be two sided.  It could also include the tagline "Velsane is all about V!" or any of the information from www.myvelsane.example.

I am uploading the other formats that I currently have for the logo.

Thank you

Target Market(s)

The representatives are teenage girls that are 13-19 but they are selling products to all ages.

Industry/Entity Type

Business

Requirements
Must have
• A field with the toll free customer service number.
The company logo.
The company website information.
The company representative name.
The company representative phone number.
The company representative email contact info.
Nice to have
• QR Code which we already have.
Should not have
• Do not make it look like a design for children. It should be modern and professional but sophisticated.

```html
<!DOCTYPE html>
<html lang="en">
<head>
<meta charset="utf-8">
<title>Velsane Business Card</title>
<link rel="stylesheet" href="https://fonts.googleapis.com/css2?family=Open+Sans:wght@400;600;700&display=swap">
<style>
  :root {
    --stage: #000000;
    --stage-glow: #1c1c1c;
    --magenta: #ee1aa9;
    --magenta-deep: #e0108f;
    --pink-soft: #f9c9e6;
    --pink-pale: #fde6f3;
    --ink: #3a3a3c;
    --white: #ffffff;
    --band-black: #050505;
  }
  html, body {
    margin: 0;
    padding: 0;
    overflow: hidden;
  }
  body {
    width: 927px;
    height: 1200px;
    position: relative;
    background: radial-gradient(ellipse at 50% 45%, var(--stage-glow) 0%, var(--stage) 70%);
    font-family: "Open Sans", sans-serif;
  }
  .card {
    position: absolute;
    border-radius: 14px;
    overflow: hidden;
    box-shadow: 0 8px 14px rgba(0,0,0,0.6);
  }
  /* Front card */
  .card--front {
    left: 150px;
    top: 133px;
    width: 656px;
    height: 397px;
    background: linear-gradient(90deg, var(--magenta) 0%, #f55cc4 40%, var(--pink-pale) 62%, var(--pink-soft) 85%, #f07cc8 100%);
  }
  .card__sheen {
    position: absolute;
    left: 0;
    top: 0;
    width: 100%;
    height: 100%;
  }
  .card__website {
    position: absolute;
    left: 0;
    right: 0;
    top: 10px;
    text-align: center;
    font-size: 43px;
    font-weight: 400;
    color: var(--ink);
    letter-spacing: 0.5px;
    white-space: nowrap;
  }
  .card__website .accent { color: var(--magenta-deep); }
  .card__contact {
    position: absolute;
    right: 14px;
    top: 118px;
    display: flex;
    flex-direction: column;
    align-items: flex-end;
    gap: 2px;
    color: var(--ink);
    white-space: nowrap;
  }
  .card__name {
    font-size: 27px;
    font-weight: 600;
    margin-right: 38px;
    line-height: 1.3;
  }
  .card__email,
  .card__rep-phone {
    font-size: 20px;
    font-weight: 400;
    line-height: 1.35;
  }
  .brand {
    position: absolute;
    display: flex;
    flex-direction: column;
    align-items: flex-end;
  }
  .brand__row {
    display: flex;
    align-items: center;
    gap: 12px;
  }
  .brand__dot {
    border-radius: 50%;
    background: var(--magenta-deep);
  }
  .brand__name {
    font-weight: 700;
    color: var(--ink);
    letter-spacing: 2px;
    line-height: 1;
  }
  .brand__url {
    font-size: 11px;
    font-weight: 700;
    color: var(--ink);
    margin-top: 4px;
  }
  .card--front .brand {
    right: 24px;
    top: 272px;
  }
  .card--front .brand__name { font-size: 60px; }
  .card--front .brand__dot { width: 22px; height: 22px; }
  /* Back card */
  .card--back {
    left: 159px;
    top: 647px;
    width: 649px;
    height: 414px;
    background: linear-gradient(110deg, var(--white) 0%, var(--pink-pale) 30%, var(--pink-soft) 65%, #ef5cbd 100%);
  }
  .card--back .brand {
    left: 0;
    right: 0;
    top: 52px;
    align-items: center;
  }
  .card--back .brand__name { font-size: 78px; }
  .card--back .brand__dot { width: 26px; height: 26px; }
  .card--back .brand__url { align-self: center; margin-left: 120px; }
  .card__wave {
    position: absolute;
    left: 0;
    bottom: 0;
    width: 649px;
    height: 190px;
  }
  .card__phone {
    position: absolute;
    left: 0;
    right: 0;
    bottom: 18px;
    text-align: center;
    font-size: 48px;
    font-weight: 700;
    color: var(--white);
    white-space: nowrap;
  }
</style>
</head>
<body>

  <section class="card card--front" aria-label="Business card front">
    <svg class="card__sheen" viewBox="0 0 656 397" aria-hidden="true">
      <path d="M0 0 H290 C400 60 430 260 300 397 H0 Z" fill="rgba(255,255,255,0.18)"/>
    </svg>
    <div class="card__website">www.<span class="accent">myvelsane</span>.example</div>
    <div class="card__contact">
      <div class="card__name">Dana Kessler</div>
      <div class="card__email">danakessler@velsane.example</div>
      <div class="card__rep-phone">(555) 014-2273</div>
    </div>
    <div class="brand">
      <div class="brand__row">
        <span class="brand__dot"></span>
        <span class="brand__name">Velsane</span>
      </div>
      <div class="brand__url">www.myvelsane.example</div>
    </div>
  </section>

  <section class="card card--back" aria-label="Business card back">
    <div class="brand">
      <div class="brand__row">
        <span class="brand__dot"></span>
        <span class="brand__name">Velsane</span>
      </div>
      <div class="brand__url">www.myvelsane.example</div>
    </div>
    <svg class="card__wave" viewBox="0 0 649 190" aria-hidden="true">
      <defs>
        <linearGradient id="waveSilver" x1="0" y1="0" x2="1" y2="0">
          <stop offset="0" stop-color="#ffffff"/>
          <stop offset="0.45" stop-color="#8a8a8a"/>
          <stop offset="0.75" stop-color="#e8e8e8"/>
          <stop offset="1" stop-color="#ffffff"/>
        </linearGradient>
      </defs>
      <path d="M0 22 C160 0 300 70 460 30 C540 10 600 2 649 6 V190 H0 Z" fill="url(#waveSilver)"/>
      <path d="M0 52 C180 30 300 90 470 55 C560 38 610 40 649 44 V190 H0 Z" fill="var(--band-black)"/>
    </svg>
    <div class="card__phone">1-800-472-Velsan.</div>
  </section>

</body>
</html>
```